" Já sou fotógrafo e possuo uma marca chamada Otávio Rangel, mais voltada para casamentos, ensaios de casais e família. Todavia já realizei muitos trabalhos no mundo corporativo, como vídeos institucionais de empresas, fotografia gastronômica, foto de carros e vídeos, foto de lojas e estabelecimentos comerciais. Daí que criei a Tulco produções para ser a empresa que irá divulgar esse tipo de material e vender por ela tais produtos de foto e filme. E por ser produções, não se ter;a um limite, poderá oferecer projetos para mídias sociais, campanhas publicitárias e afins. "

```html
<!DOCTYPE html>
<html lang="pt-BR">
<head>
<meta charset="UTF-8">
<title>Tulco Produções – Cartão de Visita</title>
<link href="https://fonts.googleapis.com/css2?family=Montserrat:wght@300;400;500&display=swap" rel="stylesheet">
<style>
  :root {
    --page-bg: #262626;
    --card-top: #2e2e2e;
    --card-bottom: #1c1c1c;
    --card-band: #353535;
    --brand-green: #3fe01f;
    --text-light: #c9c9c9;
    --text-soft: #a8a8a8;
    --icon-bg: #5a5a5a;
    --icon-fg: #e6e6e6;
  }
  * { margin: 0; padding: 0; box-sizing: border-box; }
  html, body {
    width: 1200px;
    height: 1200px;
    overflow: hidden;
    background: var(--page-bg);
    font-family: "Montserrat", Arial, sans-serif;
  }
  .canvas { position: relative; width: 1200px; height: 1200px; }

  .card {
    position: absolute;
    border-radius: 44px 10px 44px 10px;
    box-shadow: 0 6px 18px rgba(0,0,0,0.55);
    overflow: hidden;
  }
  .card-surface {
    position: absolute;
    inset: 0;
    background: linear-gradient(160deg, var(--card-top) 0%, var(--card-band) 45%, var(--card-bottom) 100%);
  }

  .card-front { left: 355px; top: 233px; width: 617px; height: 331px; }
  .card-back  { left: 235px; top: 605px; width: 850px; height: 365px; }

  .brand {
    position: absolute;
    display: flex;
    flex-direction: column;
    align-items: center;
    color: var(--brand-green);
    font-weight: 400;
  }
  .brand-dot {
    width: 18px; height: 18px;
    border-radius: 50%;
    background: var(--brand-green);
    margin-bottom: 14px;
  }
  .brand-name { font-size: 60px; letter-spacing: 4px; line-height: 1; }
  .brand-line { font-size: 15px; letter-spacing: 10px; margin-top: 8px; padding-left: 10px; }

  .card-front .brand { left: 0; right: 0; top: 92px; }
  .card-back .brand { left: 70px; top: 68px; }
  .card-back .brand-name { font-size: 56px; }

  .contact-list {
    position: absolute;
    left: 0; top: 0;
    list-style: none;
  }
  .contact-item {
    position: absolute;
    display: flex;
    align-items: center;
    gap: 14px;
    color: var(--text-light);
    font-size: 11.5px;
    line-height: 1.45;
    letter-spacing: 0.4px;
    white-space: nowrap;
  }
  .contact-icon {
    flex: none;
    width: 30px; height: 30px;
    border-radius: 50%;
    background: var(--icon-bg);
    display: flex; align-items: center; justify-content: center;
  }
  .contact-icon svg { width: 16px; height: 16px; }
  .contact-text { color: var(--text-soft); }

  .contact-email   { left: 410px; top: 90px; }
  .contact-phone   { left: 398px; top: 141px; }
  .contact-address { left: 386px; top: 200px; }
  .contact-web     { left: 374px; top: 262px; }
</style>
</head>
<body>
<main class="canvas">

  <section class="card card-front" aria-label="Frente do cartão">
    <div class="card-surface" role="img" aria-label="Superfície escura com textura de listras diagonais"></div>
    <div class="brand">
      <span class="brand-dot"></span>
      <span class="brand-name">TULCO</span>
      <span class="brand-line">PRODUÇÕES</span>
    </div>
  </section>

  <section class="card card-back" aria-label="Verso do cartão">
    <div class="card-surface" role="img" aria-label="Superfície escura com textura de listras diagonais"></div>
    <div class="brand">
      <span class="brand-dot"></span>
      <span class="brand-name">TULCO</span>
      <span class="brand-line">PRODUÇÕES</span>
    </div>

    <ul class="contact-list">
      <li class="contact-item contact-email">
        <span class="contact-icon">
          <svg viewBox="0 0 16 16" fill="none" stroke="var(--icon-fg)" stroke-width="1.4"><rect x="2" y="4" width="12" height="8" rx="1"/><path d="M2 4.5l6 4.5 6-4.5"/></svg>
        </span>
        <span class="contact-text">CONTATO@TULCOPROD.COM</span>
      </li>
      <li class="contact-item contact-phone">
        <span class="contact-icon">
          <svg viewBox="0 0 16 16" fill="var(--icon-fg)"><path d="M4.2 2.2l2 2.3-1.1 1.5a8 8 0 0 0 4.9 4.9l1.5-1.1 2.3 2-1.2 1.9C7.6 13.4 2.6 8.4 2.3 3.4z"/></svg>
        </span>
        <span class="contact-text">+55 21 4093 2718<br>+55 21 9862 5031</span>
      </li>
      <li class="contact-item contact-address">
        <span class="contact-icon">
          <svg viewBox="0 0 16 16" fill="var(--icon-fg)"><path d="M8 2.5l6 5.2h-1.8V13H9.4V9.8H6.6V13H3.8V7.7H2z"/></svg>
        </span>
        <span class="contact-text">RUA DAS LARANJEIRAS 210<br>RIO DE JANEIRO, BRASIL</span>
      </li>
      <li class="contact-item contact-web">
        <span class="contact-icon">
          <svg viewBox="0 0 16 16" fill="none" stroke="var(--icon-fg)" stroke-width="1.2"><circle cx="8" cy="8" r="5.8"/><ellipse cx="8" cy="8" rx="2.5" ry="5.8"/><path d="M2.2 8h11.6"/></svg>
        </span>
        <span class="contact-text">WWW.TULCOPROD.COM</span>
      </li>
    </ul>
  </section>

</main>
</body>
</html>
```